Webdesign for an Health & Beauty Center

We need a new modern and elegant web design for the relaunch of the http://kirelta.at/ website.
The website is for a company which offer all services for a beuty center like epilation, cosmetics and more.
The new website should use big emotional background images and a modern menu.
All in all the website should give a female expression and the design should be clear and not playful.
The existing logo used be used for the new design, the base colours of the existing website could be used optionally.

Industry/Entity Type
It Company
Look and feel
Each slider illustrates characteristics of the customer's brand and the style your logo design should communicate.

```html
<!DOCTYPE html>
<html lang="en">
<head>
<meta charset="utf-8">
<title>Kirelta – health &amp; beauty center</title>
<link href="https://fonts.googleapis.com/css2?family=Questrial&family=Open+Sans:wght@400;700&display=swap" rel="stylesheet">
<style>
:root{
  --gold:#b8923f;
  --gold-light:#c9a45a;
  --cream:#f2e9db;
  --line:#d8cbb6;
  --text:#3a3128;
  --heading:#2f2a24;
  --footer:#4d4233;
  --footer-text:#cbb98f;
  --white:#ffffff;
}
*{margin:0;padding:0;box-sizing:border-box}
html,body{width:877px;height:1200px;overflow:hidden}
body{position:relative;background:var(--cream);font-family:"Open Sans",sans-serif;color:var(--text)}
.abs{position:absolute}
.site-header{position:absolute;left:0;top:0;width:877px;height:80px;background:var(--white);border-bottom:1px solid #e6ddd0}
.brand{position:absolute;left:126px;top:12px;font-family:"Questrial",sans-serif;color:var(--gold-light);font-weight:400}
.brand-name{font-size:34px;letter-spacing:3px;line-height:38px}
.brand-tag{font-size:14px;line-height:16px;letter-spacing:.3px}
.main-nav{position:absolute;top:39px;font-size:8.6px;letter-spacing:.2px;color:var(--heading)}
.main-nav span{position:absolute;white-space:nowrap}
.main-nav .active{color:var(--gold)}
.main-nav .strong{font-weight:700}
.nav-underline{position:absolute;left:444px;top:62px;width:73px;height:2px;background:var(--gold)}
.hero{position:absolute;left:0;top:80px;width:877px;height:383px;
  background:linear-gradient(100deg,#b9a57a 0%,#d9b79a 22%,#caa085 45%,#e3c0a6 65%,#b98a6d 85%,#8a6a52 100%)}
.section-title{position:absolute;font-family:"Questrial",sans-serif;font-size:16px;color:var(--heading)}
.rule{position:absolute;height:1px;background:var(--line)}
.rule::after{content:"";position:absolute;left:41px;top:1px;border-left:4px solid transparent;border-right:4px solid transparent;border-top:4px solid var(--line)}
.subhead{position:absolute;left:80px;top:521px;font-family:"Questrial",sans-serif;font-size:16px;color:var(--heading)}
.para{position:absolute;left:80px;width:426px;font-size:8px;line-height:11px;text-align:justify}
.thumb{position:absolute;left:80px;top:658px;width:179px;height:123px;background:linear-gradient(135deg,#b07d4d,#d3a876 50%,#efe6d8)}
.links span{position:absolute;left:290px;font-size:8px;text-decoration:underline;white-space:nowrap}
.bullet{position:absolute;width:6px;height:6px;border-radius:50%;border:1.5px solid var(--gold-light)}
.avatar{position:absolute;left:566px;width:48px;height:48px}
.testi{position:absolute;left:627px;width:170px;font-size:8px;line-height:11.5px}
.testi b{font-size:9.5px;color:var(--heading)}
.testi small{font-size:8px}
.tip-num{position:absolute;left:80px;width:43px;height:43px;background:var(--gold);color:var(--white);font-family:"Questrial",sans-serif;font-size:16px;display:flex;align-items:center;justify-content:center}
.tip{position:absolute;left:148px;width:358px;font-size:8px;line-height:11.5px;text-align:justify}
.tip b{display:block;font-size:9.5px;color:var(--heading);line-height:13px}
.products span{position:absolute;left:584px;font-size:8px;letter-spacing:.3px}
.site-footer{position:absolute;left:0;top:1083px;width:877px;height:117px;background:var(--footer)}
.social{position:absolute;top:1125px;width:19px;height:19px;border-radius:50%;background:#8f7f5e}
.copyright{position:absolute;top:1157px;left:0;width:877px;text-align:center;font-size:8px;color:var(--footer-text)}
</style>
</head>
<body>
<header class="site-header">
  <div class="brand"><div class="brand-name">kirelta</div><div class="brand-tag">health &amp; beauty center</div></div>
  <nav class="main-nav">
    <span style="left:392px">UBER UNS</span>
    <span class="active" style="left:455px">LEISTUNGEN</span>
    <span style="left:529px">GALERIE</span>
    <span class="strong" style="left:585px">PFLEGELINIE</span>
    <span style="left:657px">ANGEBOTE</span>
    <span style="left:723px">PREISLISTEN</span>
    <span style="left:794px">KONTAKT</span>
  </nav>
  <div class="nav-underline"></div>
  <svg class="abs" style="left:476px;top:63px" width="8" height="5"><polygon points="0,0 8,0 4,5" fill="#b8923f"/></svg>
</header>

<div class="hero" role="img" aria-label="Woman receiving a back massage beside a candle and wicker ball"></div>

<h2 class="section-title" style="left:80px;top:478px">About Kirelta</h2>
<div class="rule" style="left:80px;top:509px;width:426px"></div>
<h3 class="subhead">Lorem ipsum dolor sit amet, consectetur</h3>
<p class="para" style="top:550px">Nulla id justo egestas, vestibulum nibh quis, fringilla justo. Pellentesque lobortis pharetra orci, a pulvinar quam pretium nec. Donec auctor elit et nunc mattis dignissim. Vestibulum adipiscing nibh lectus, ut fringilla ligula tincidunt at. Ut ut arcu id tellus imperdiet dapibus eu id lacus. Cras orci enim,</p>
<p class="para" style="top:594px">pellentesque non faucibus at, eleifend at quam. Morbi sit amet viverra nibh. Curabitur feugiat massa at lobortis consequat. Fusce gravida feuamet leo gravida, eu varius felis consectetur. Quisque lacinia tellu Aliquam odio nibh, pulvinar quis aliquam quis, tincidunt non odio. Prae Aliquam odio nibh, pulvinar quis aliquam quis, tincidunt non odio. Praeasdas asd egrrhgh dsdfsdd.</p>
<div class="thumb" role="img" aria-label="Spa still life with lily, towel and stones on bamboo"></div>
<div class="links">
  <i class="bullet" style="left:274px;top:661px"></i><span style="top:658px">Lorem Ipsume Hgaagj yiern jivsmk kha sd lku&nbsp; dsadee</span>
  <i class="bullet" style="left:274px;top:687px"></i><span style="top:684px">Lorem Pingo Lkateche Ipsume Hgaagj yiern jivsm</span>
  <i class="bullet" style="left:274px;top:716px"></i><span style="top:713px">felis consectetur. Quisque lacinia tellu Aliquam io nibh</span>
  <i class="bullet" style="left:274px;top:744px"></i><span style="top:741px">Giat dolor.sent elementuyiyi nhgten gh llk lkljm libero</span>
  <i class="bullet" style="left:274px;top:771px"></i><span style="top:768px">Nulla id justo egestas, vestibulum nibh quis</span>
</div>

<h2 class="section-title" style="left:564px;top:478px">Testimonials</h2>
<div class="rule" style="left:564px;top:509px;width:232px"></div>
<div class="avatar" role="img" aria-label="Client portrait" style="top:524px;background:linear-gradient(#e9d2c0,#c99c80)"></div>
<div class="testi" style="top:524px"><b>Client Name,</b> <small>Date</small><br>“Lorem Ipsume Hgaagj yiern jivsmkhagae latur eeruisque lacinia tellu Aliquam odio nibh, pulvinar quis aliqua”</div>
<div class="avatar" role="img" aria-label="Client portrait" style="top:594px;background:linear-gradient(#7a2a22,#c07a5e)"></div>
<div class="testi" style="top:594px;color:#111"><b>Client Name,</b> <small>Date</small><br>“Lorem Ipsume Hgaagj yiern jivsmkhagae latur eeruisque lacinia tellu Aliquam odio nibh, pulvinar quis aliqua”</div>
<div class="avatar" role="img" aria-label="Client portrait" style="top:664px;background:linear-gradient(#e8e4e0,#6b5848)"></div>
<div class="testi" style="top:664px"><b>Client Name,</b> <small>Date</small><br>“Lorem Ipsume Hgaagj yiern jivsmkhagae latur eeruisque lacinia tellu Aliquam odio nibh, pulvinar quis aliqua”</div>
<div class="avatar" role="img" aria-label="Client portrait" style="top:734px;background:linear-gradient(#b4683a,#e8c0a0)"></div>
<div class="testi" style="top:734px"><b>Client Name,</b> <small>Date</small><br>“Lorem Ipsume Hgaagj yiern jivsmkhagae latur eeruisque lacinia tellu Aliquam odio nibh, pulvinar quis aliqua”</div>

<h2 class="section-title" style="left:80px;top:812px">Important Tips</h2>
<div class="rule" style="left:80px;top:843px;width:426px"></div>
<div class="tip-num" style="top:861px">1</div>
<div class="tip" style="top:860px"><b>Nulla id justo egestas</b>vestibulum nibh quis, fringilla justo. Pellentesque lobortis pharetra orci, a pulvinar quam pretium nec. Donec auctor elit et nunc mattis dignissim. Vestibulum adipiscing nibh lectus, ut fringilla ligula tincidunt at.</div>
<div class="tip-num" style="top:931px">2</div>
<div class="tip" style="top:929px"><b>Nulla id justo machiloee egbidra estas</b>vestibulum nibh quis, fringilla justo. Pellentesque lobortis pharetra orci, a pulvinar quam pretium nec. Donec auctor elit et nunc mattis dignissim. Vestibulum adipiscing nibh lectus, ut fringilla ligula tincidunt at.</div>
<div class="tip-num" style="top:1001px">3</div>
<div class="tip" style="top:999px"><b>Lorem Ipsum te usto machiloee egbidra estas</b>vestibulum nibh quis, fringilla justo. Pellentesque lobortis pharetra orci, a pulvinar quam pretium nec. Donec auctor elit et nunc mattis dignissim. Vestibulum adipiscing nibh lectus, ut fringilla ligula tincidunt at.</div>

<h2 class="section-title" style="left:566px;top:812px">Products for your life</h2>
<div class="rule" style="left:564px;top:843px;width:232px"></div>
<div class="products">
  <i class="bullet" style="left:568px;top:862px"></i><span style="top:859px">HAIR CARE</span>
  <i class="bullet" style="left:568px;top:888px"></i><span style="top:885px">STYLING</span>
  <i class="bullet" style="left:568px;top:914px"></i><span style="top:911px">SKIN CARE</span>
  <i class="bullet" style="left:568px;top:940px"></i><span style="top:937px">BODY</span>
  <i class="bullet" style="left:568px;top:966px"></i><span style="top:963px">MEN</span>
  <i class="bullet" style="left:568px;top:992px"></i><span style="top:989px">WOMEN</span>
  <i class="bullet" style="left:568px;top:1018px"></i><span style="top:1015px">MAKEUP</span>
  <i class="bullet" style="left:568px;top:1044px"></i><span style="top:1041px">GIFTS</span>
</div>

<footer class="site-footer"></footer>
<span class="social" style="left:391px"></span>
<span class="social" style="left:417px"></span>
<span class="social" style="left:443px"></span>
<span class="social" style="left:468px"></span>
<p class="copyright">Copyright © 2014 kirelta health &amp; beauty center. All rights are reserved.</p>
</body>
</html>
```